Real Estate Company / Capital Needs Cards!

need business cards designed using the logos that were just designed by brightquill.

Target Market(s)

Investors and clients looking to purchase real estate or invest in the business.

Industry/Entity Type

Business

Requirements
Must have
• two designs - one for the real estate logo and one for the capital logo, similar but slightly different.
Nice to have
• something to make it pop (perhaps on the back)
Should not have
• much color

```html
<!DOCTYPE html>
<html lang="en">
<head>
<meta charset="utf-8">
<title>Halden Capital — Business Cards</title>
<link href="https://fonts.googleapis.com/css2?family=Arimo:wght@400;700&family=Oswald:wght@500;600&display=swap" rel="stylesheet">
<style>
  :root {
    --page: #ffffff;
    --cream: #f4e4bf;
    --cream-soft: #e9d6aa;
    --ink-white: #f2f2f2;
    --ink-grey: #c9c9c9;
    --band: #050505;
    --card-top: #5c5c5c;
    --card-bottom: #2d2d2d;
    --outer-dark: #2f2f2f;
    --solid-black: #1b1b1b;
    --gold-top: #e3bf83;
    --gold-mid: #c38a34;
    --gold-bottom: #ddb272;
    --white: #ffffff;
  }
  * { margin: 0; padding: 0; box-sizing: border-box; }
  html, body {
    width: 1200px; height: 900px; overflow: hidden;
    background: var(--page);
    font-family: "Arimo", Arial, sans-serif;
  }
  .sheet { position: relative; width: 1200px; height: 900px; }
  .card { position: absolute; width: 382px; height: 218px; overflow: hidden; }

  /* brand lockup */
  .brand { position: absolute; display: flex; flex-direction: column; align-items: center; color: var(--cream); font-weight: 400; }
  .brand__square { width: 40px; height: 40px; background: var(--cream); border-radius: 4px; margin-bottom: 6px; }
  .brand__name { font-size: 22px; letter-spacing: 1px; line-height: 1; }
  .brand__sub { font-size: 8.5px; letter-spacing: 1.4px; margin-top: 3px; line-height: 1; }
  .brand--white { color: var(--white); }
  .brand--white .brand__square { background: var(--white); }

  /* front A */
  .card--front-a { left: 188px; top: 224px; background: linear-gradient(180deg, var(--card-top), var(--card-bottom)); }
  .card--front-a .brand { left: 14px; top: 12px; }
  .name-band { position: absolute; left: 0; top: 105px; width: 196px; height: 64px; }
  .name-band__text { position: absolute; left: 17px; top: 118px; }
  .person-name { font-size: 20px; color: var(--ink-grey); line-height: 1; letter-spacing: 0.3px; }
  .person-name strong { color: var(--ink-white); font-weight: 400; }
  .person-role { font-size: 10px; color: var(--ink-white); margin-top: 4px; letter-spacing: 0.3px; }
  .address-a { position: absolute; left: 18px; top: 176px; font-size: 10.5px; color: var(--ink-white); line-height: 1.25; }
  .contact-a { position: absolute; right: 17px; top: 123px; text-align: right; }
  .phone-big { font-family: "Oswald", "Arial Narrow", sans-serif; font-weight: 600; font-size: 24px; color: var(--cream); line-height: 1; letter-spacing: 0.2px; }
  .contact-a__line { font-size: 11px; color: var(--ink-white); line-height: 1.25; letter-spacing: 0.4px; }
  .contact-a__line:first-of-type { margin-top: 4px; }

  /* front B */
  .card--front-b { left: 639px; top: 226px; background: var(--outer-dark); }
  .card--front-b .panel { position: absolute; left: 0; top: 0; }
  .card--front-b .brand { right: 26px; top: 28px; }
  .card--front-b .brand__square { width: 44px; height: 44px; }
  .person-b { position: absolute; left: 29px; top: 98px; }
  .person-b__name { font-family: "Oswald", "Arial Narrow", sans-serif; font-weight: 600; font-size: 17px; color: var(--cream); line-height: 1; }
  .person-b__role { font-size: 10px; color: var(--ink-grey); margin-top: 2px; letter-spacing: 0.3px; }
  .details { position: absolute; left: 29px; top: 139px; list-style: none; }
  .details li { display: flex; align-items: center; font-size: 8.5px; color: var(--ink-white); height: 13px; letter-spacing: 0.3px; }
  .details__key { width: 9px; height: 9px; background: var(--cream); color: #333; font-size: 6.5px; font-weight: 700; display: inline-flex; align-items: center; justify-content: center; margin-right: 5px; }
  .address-b { position: absolute; right: 27px; top: 163px; text-align: right; font-size: 8.5px; color: var(--ink-grey); line-height: 1.35; letter-spacing: 0.3px; }

  /* backs */
  .card--back-black { left: 185px; top: 467px; background: var(--solid-black); }
  .card--back-gold { left: 645px; top: 467px; background: linear-gradient(180deg, var(--gold-top) 0%, var(--gold-mid) 58%, var(--gold-bottom) 100%); }
  .card--back-black .brand, .card--back-gold .brand { left: 0; right: 0; top: 57px; }
</style>
</head>
<body>
<main class="sheet">

  <section class="card card--front-a" aria-label="Front, version one">
    <div class="brand">
      <span class="brand__square"></span>
      <span class="brand__name">HALDEN</span>
      <span class="brand__sub">CAPITAL, LLC</span>
    </div>
    <svg class="name-band" width="196" height="64" viewBox="0 0 196 64" aria-hidden="true">
      <polygon points="0,0 183,0 183,22 196,30 183,36 183,64 0,64" fill="var(--band)"/>
    </svg>
    <div class="name-band__text">
      <p class="person-name">XYZNS <strong>NAME</strong></p>
      <p class="person-role">XYY DESIGNATION</p>
    </div>
    <p class="address-a">3546, lorem ipsum country,<br>city 56487 lorem ipsum.</p>
    <div class="contact-a">
      <p class="phone-big">000-111-2222</p>
      <p class="contact-a__line">www.loremipsum.com</p>
      <p class="contact-a__line">loremipsum@mailbox.com</p>
    </div>
  </section>

  <section class="card card--front-b" aria-label="Front, version two">
    <svg class="panel" width="382" height="218" viewBox="0 0 382 218" aria-hidden="true">
      <defs>
        <linearGradient id="panelShade" x1="0" y1="0" x2="0" y2="1">
          <stop offset="0" stop-color="#6b6b6b"/>
          <stop offset="0.45" stop-color="#3e3e3e"/>
          <stop offset="1" stop-color="#222222"/>
        </linearGradient>
      </defs>
      <path d="M17,6 H330 L376,42 V200 Q376,212 364,212 H17 Q6,212 6,200 V18 Q6,6 17,6 Z" fill="url(#panelShade)" stroke="#555" stroke-width="1"/>
    </svg>
    <div class="brand">
      <span class="brand__square"></span>
      <span class="brand__name">HALDEN</span>
      <span class="brand__sub">CAPITAL, LLC</span>
    </div>
    <div class="person-b">
      <p class="person-b__name">XYZSH NAME</p>
      <p class="person-b__role">XYZ. DESIGNATION</p>
    </div>
    <ul class="details">
      <li><span class="details__key">T</span>000-111-2222</li>
      <li><span class="details__key">F</span>+0000-334-4444</li>
      <li><span class="details__key">E</span>LOREMIPSUM@MAILBOX.COM</li>
      <li><span class="details__key">W</span>WWW.LOREMIPSUM.COM</li>
    </ul>
    <p class="address-b">3546, LOREM IPSUM COUNTRY,<br>CITY 56487</p>
  </section>

  <section class="card card--back-black" aria-label="Back, black">
    <div class="brand">
      <span class="brand__square"></span>
      <span class="brand__name">HALDEN</span>
      <span class="brand__sub">CAPITAL, LLC</span>
    </div>
  </section>

  <section class="card card--back-gold" aria-label="Back, gold">
    <div class="brand brand--white">
      <span class="brand__square"></span>
      <span class="brand__name">HALDEN</span>
      <span class="brand__sub">CAPITAL, LLC</span>
    </div>
  </section>

</main>
</body>
</html>
```